Wren Sporting Goods Inc.

Need to create a website that is informational and has the ability to sell goods and services. Such as a custom t shirt designer where the user can upload and image to be displayed on the garmet. The sports we specialize in are basketball, football, and baseball.

Would like like:
Home Page
Locker Room Page:
Custom Uniforms Page
Custom Shirt Creator
Brands
About

Competitor websites are
tundrafieldwearnx.com
dvq.com
lumarogear.com

```html
<!DOCTYPE html>
<html lang="en">
<head>
<meta charset="utf-8">
<title>Wren Sporting Goods</title>
<link href="https://fonts.googleapis.com/css2?family=Montserrat:wght@600;700;800&family=Inter:wght@400;500;600;700&display=swap" rel="stylesheet">
<style>
:root{
  --red:#d2433f;
  --red-light:#e06460;
  --blue:#2a64b3;
  --ink:#0b0b0b;
  --text:#1c1c1c;
  --tint:#f6f3f3;
  --line:#9a9a9a;
  --white:#ffffff;
}
*{margin:0;padding:0;box-sizing:border-box}
html,body{width:1200px;height:3292px;overflow:hidden}
body{font-family:'Inter',sans-serif;color:var(--text);background:var(--white);position:relative}
.abs{position:absolute}
.head{font-family:'Montserrat',sans-serif;font-weight:800}

/* header + hero */
.hero{position:absolute;left:0;top:0;width:1200px;height:672px;background:var(--ink);overflow:hidden}
.brand{position:absolute;left:38px;top:36px;display:flex;align-items:center;gap:10px;z-index:3}
.brand-mark{width:34px;height:34px;border-radius:50%;background:var(--blue);flex:none}
.brand-name{font-family:'Montserrat',sans-serif;font-weight:800;font-size:16px;color:var(--white);line-height:1;white-space:nowrap}
.nav{position:absolute;left:380px;top:35px;display:flex;align-items:center;z-index:3}
.nav a{font-family:'Inter',sans-serif;font-size:13px;color:var(--white);text-decoration:none;padding:9px 13px;text-transform:uppercase;white-space:nowrap}
.nav a.is-active{background:var(--red)}
.tools{position:absolute;left:1091px;top:40px;display:flex;gap:24px;z-index:3}
.hero-text{z-index:2;white-space:nowrap}
.hero-kicker{left:122px;top:160px;font-size:49px;color:var(--blue);line-height:1}
.hero-title{left:120px;top:210px;font-size:90px;color:var(--red);line-height:1}
.hero-sub{left:122px;top:300px;font-size:47px;color:var(--white);line-height:1;letter-spacing:-.3px}
.hero-copy{left:122px;top:372px;width:360px;font-size:14.5px;line-height:25px;color:#e8e8e8;white-space:normal}
.btn-hero{left:122px;top:449px;width:298px;height:54px;background:var(--red);color:var(--white);font-family:'Montserrat',sans-serif;font-weight:800;font-size:16px;display:flex;align-items:center;justify-content:center}
.hero-photo{left:560px;top:105px;width:535px;height:567px;background:radial-gradient(ellipse at 50% 55%,#d8302f 0%,#b52427 38%,#2a1514 72%,var(--ink) 100%);z-index:1}
.hero-band{left:0;top:560px;z-index:1}
.hero-badge{left:730px;top:590px;width:80px;height:80px;border-radius:50%;background:var(--white);border:6px solid var(--blue);z-index:2}

/* specialists */
.section-title{font-family:'Montserrat',sans-serif;font-weight:800;font-size:32px;color:var(--ink);text-align:center;width:1200px;left:0}
.rule{height:2px;width:54px;background:var(--red)}
.sport-card{top:872px;width:246px;height:188px;border:1px solid var(--ink);display:flex;flex-direction:column;align-items:center;padding-top:36px}
.sport-card span{margin-top:26px;font-size:18px;font-weight:500;letter-spacing:.3px}

/* product rows */
.band{left:0;width:1200px}
.band--tint{background:var(--tint)}
.row-title{left:150px;font-size:33px;color:var(--ink);letter-spacing:.5px}
.btn-view{left:945px;width:105px;height:41px;background:var(--blue);color:var(--white);font-family:'Montserrat',sans-serif;font-weight:600;font-size:14px;display:flex;align-items:center;justify-content:center}
.arrow{width:41px;height:41px;border:1.5px solid #666;border-radius:50%;display:flex;align-items:center;justify-content:center}
.product{width:200px;display:flex;flex-direction:column;align-items:center}
.product-img{width:160px;height:160px;border-radius:14px}
.product-name{margin-top:36px;font-size:15px}
.product-price{margin-top:8px;font-size:16px;font-weight:700}
.btn-cart{margin-top:17px;width:103px;height:27px;background:var(--red);color:var(--white);font-family:'Montserrat',sans-serif;font-weight:700;font-size:10.5px;display:flex;align-items:center;justify-content:center}

/* brands */
.partners{left:160px;top:2806px;width:890px;display:flex;justify-content:space-between;align-items:center}
.partners span{font-family:'Inter',sans-serif;font-weight:600;font-size:19px;color:#3a3a3a}

/* footer */
.footer{left:0;top:2915px;width:1200px;height:377px;background:var(--ink)}
.footer-brand{left:0;top:2985px;width:1200px;display:flex;justify-content:center;align-items:center;gap:16px}
.footer-brand .brand-mark{width:62px;height:62px}
.footer-brand .brand-name{font-size:40px}
.footer-nav{left:0;top:3105px;width:1200px;display:flex;justify-content:center}
.footer-nav a{color:var(--white);text-decoration:none;font-size:13.5px;padding:0 13px}
.follow{left:0;top:3166px;width:1200px;display:flex;justify-content:center;align-items:center;gap:6px;color:var(--white);font-size:13.5px}
.follow .social{width:27px;height:27px;border-radius:50%;background:var(--white)}
.follow b{font-weight:400;margin-right:12px}
.copyright{left:0;top:3238px;width:1200px;text-align:center;color:var(--white);font-size:13px}
</style>
</head>
<body>

<header class="hero">
  <div class="brand"><div class="brand-mark"></div><div class="brand-name">WREN SPORTING GOODS</div></div>
  <nav class="nav">
    <a class="is-active">Home</a><a>Locker Room</a><a>Custom Uniforms</a><a>Custom Shirt Creator</a><a>Brands</a><a>About</a>
  </nav>
  <div class="tools">
    <svg width="20" height="20" viewBox="0 0 20 20" fill="none" stroke="#fff" stroke-width="2"><circle cx="8" cy="8" r="6.5"/><line x1="13" y1="13" x2="19" y2="19"/></svg>
    <svg width="20" height="20" viewBox="0 0 20 20" fill="none" stroke="#fff" stroke-width="1.8"><path d="M1 2h3l2 10h10l2-7H5"/><circle cx="8" cy="16" r="1.5"/><circle cx="15" cy="16" r="1.5"/></svg>
  </div>

  <div class="abs hero-photo" role="img" aria-label="Athlete in a red sports t-shirt standing with hands on hips"></div>

  <div class="abs head hero-text hero-kicker">SPORTS</div>
  <div class="abs head hero-text hero-title">T SHIRT</div>
  <div class="abs head hero-text hero-sub">CUSTOM DESIGN</div>
  <p class="abs hero-text hero-copy">c iste natus error sit volupt atem accu san tium doloremque laudantium.</p>
  <div class="abs hero-text btn-hero">VIEW MORE LOCKER ROOM</div>

  <svg class="abs hero-band" width="1200" height="112" viewBox="0 0 1200 112">
    <polygon points="0,0 700,112 0,112" fill="var(--red-light)"/>
    <polygon points="0,28 680,112 0,112" fill="var(--red)"/>
    <polygon points="1200,58 900,112 1200,112" fill="var(--red)"/>
    <polygon points="0,90 1200,90 1200,112 0,112" fill="var(--red)" opacity=".6"/>
  </svg>
  <div class="abs hero-badge"></div>
</header>

<h2 class="abs section-title" style="top:750px">YOUR TEAM SPORTS SPECIALISTS</h2>
<div class="abs rule" style="left:573px;top:820px"></div>

<div class="abs sport-card" style="left:202px">
  <svg width="60" height="60" viewBox="0 0 60 60" fill="none" stroke="var(--blue)" stroke-width="3"><circle cx="30" cy="30" r="27"/><path d="M30 3v54M3 30h54M12 10c10 10 10 30 0 40M48 10c-10 10-10 30 0 40"/></svg>
  <span>BASKETBALL</span>
</div>
<div class="abs sport-card" style="left:478px">
  <svg width="60" height="60" viewBox="0 0 60 60" fill="none" stroke="var(--blue)" stroke-width="3"><circle cx="30" cy="30" r="27"/><polygon points="30,20 40,27 36,39 24,39 20,27" fill="var(--blue)"/><path d="M30 20V6M40 27l13-4M36 39l8 11M24 39l-8 11M20 27L7 23"/></svg>
  <span>FOOTBALL</span>
</div>
<div class="abs sport-card" style="left:752px">
  <svg width="60" height="60" viewBox="0 0 60 60" fill="none" stroke="var(--blue)" stroke-width="3"><circle cx="30" cy="30" r="27"/><path d="M12 10c8 12 8 28 0 40M48 10c-8 12-8 28 0 40"/></svg>
  <span>BASEBALL</span>
</div>

<!-- Basketball -->
<section class="abs band band--tint" style="top:1123px;height:505px"></section>
<h2 class="abs head row-title" style="top:1172px">BASKETBALL</h2>
<div class="abs rule" style="left:151px;top:1223px"></div>
<div class="abs btn-view" style="top:1174px">VIEW ALL</div>
<div class="abs arrow" style="left:53px;top:1370px"><svg width="12" height="16" viewBox="0 0 12 16" fill="none" stroke="#555" stroke-width="1.5"><path d="M9 1L2 8l7 7"/></svg></div>
<div class="abs arrow" style="left:1104px;top:1370px"><svg width="12" height="16" viewBox="0 0 12 16" fill="none" stroke="#555" stroke-width="1.5"><path d="M3 1l7 7-7 7"/></svg></div>
<div class="abs product" style="left:132px;top:1275px"><div class="product-img" role="img" aria-label="Orange basketball" style="background:radial-gradient(circle at 40% 35%,#e9843f,#b84e1c)"></div><div class="product-name">Lorem ipsum dolor sit</div><div class="product-price">$25.99</div><div class="btn-cart">ADD TO CART</div></div>
<div class="abs product" style="left:372px;top:1275px"><div class="product-img" role="img" aria-label="Navy blue athletic t-shirt" style="background:linear-gradient(#2f4d8a,#1d3466)"></div><div class="product-name">Lorem ipsum dolor sit</div><div class="product-price">$25.99</div><div class="btn-cart">ADD TO CART</div></div>
<div class="abs product" style="left:632px;top:1275px"><div class="product-img" role="img" aria-label="Basketball" style="background:radial-gradient(circle at 40% 35%,#e2703d,#a9411c)"></div><div class="product-name">Lorem ipsum dolor sit</div><div class="product-price">$25.99</div><div class="btn-cart">ADD TO CART</div></div>
<div class="abs product" style="left:879px;top:1275px"><div class="product-img" role="img" aria-label="Black athletic t-shirt" style="background:linear-gradient(#2a2a2a,#0d0d0d)"></div><div class="product-name">Lorem ipsum dolor sit</div><div class="product-price">$25.99</div><div class="btn-cart">ADD TO CART</div></div>

<!-- Football -->
<h2 class="abs head row-title" style="top:1676px">FOOTBALL</h2>
<div class="abs rule" style="left:151px;top:1727px"></div>
<div class="abs btn-view" style="top:1679px">VIEW ALL</div>
<div class="abs arrow" style="left:53px;top:1873px"><svg width="12" height="16" viewBox="0 0 12 16" fill="none" stroke="#555" stroke-width="1.5"><path d="M9 1L2 8l7 7"/></svg></div>
<div class="abs arrow" style="left:1104px;top:1873px"><svg width="12" height="16" viewBox="0 0 12 16" fill="none" stroke="#555" stroke-width="1.5"><path d="M3 1l7 7-7 7"/></svg></div>
<div class="abs product" style="left:132px;top:1779px"><div class="product-img" role="img" aria-label="Soccer ball" style="background:radial-gradient(circle,#f2efe8,#9c9890)"></div><div class="product-name">Lorem ipsum dolor sit</div><div class="product-price">$25.99</div><div class="btn-cart">ADD TO CART</div></div>
<div class="abs product" style="left:372px;top:1779px"><div class="product-img" role="img" aria-label="Maroon football helmet" style="background:radial-gradient(circle at 55% 40%,#b3243c,#6d1423)"></div><div class="product-name">Lorem ipsum dolor sit</div><div class="product-price">$25.99</div><div class="btn-cart">ADD TO CART</div></div>
<div class="abs product" style="left:632px;top:1779px"><div class="product-img" role="img" aria-label="Black and white soccer ball" style="background:radial-gradient(circle,#e8e8e8,#7a7a7a)"></div><div class="product-name">Lorem ipsum dolor sit</div><div class="product-price">$25.99</div><div class="btn-cart">ADD TO CART</div></div>
<div class="abs product" style="left:879px;top:1779px"><div class="product-img" role="img" aria-label="Navy polo shirt" style="background:linear-gradient(#263a63,#141f3a)"></div><div class="product-name">Lorem ipsum dolor sit</div><div class="product-price">$25.99</div><div class="btn-cart">ADD TO CART</div></div>

<!-- Baseball -->
<section class="abs band band--tint" style="top:2140px;height:478px"></section>
<h2 class="abs head row-title" style="top:2186px">BASEBALL</h2>
<div class="abs rule" style="left:151px;top:2236px"></div>
<div class="abs btn-view" style="top:2188px">VIEW ALL</div>
<div class="abs arrow" style="left:53px;top:2365px"><svg width="12" height="16" viewBox="0 0 12 16" fill="none" stroke="#555" stroke-width="1.5"><path d="M9 1L2 8l7 7"/></svg></div>
<div class="abs arrow" style="left:1104px;top:2365px"><svg width="12" height="16" viewBox="0 0 12 16" fill="none" stroke="#555" stroke-width="1.5"><path d="M3 1l7 7-7 7"/></svg></div>
<div class="abs product" style="left:132px;top:2272px"><div class="product-img" role="img" aria-label="Baseball with red stitching" style="background:radial-gradient(circle,#f4f1ec,#c7c2bb)"></div><div class="product-name">Lorem ipsum dolor sit</div><div class="product-price">$25.99</div><div class="btn-cart">ADD TO CART</div></div>
<div class="abs product" style="left:372px;top:2272px"><div class="product-img" role="img" aria-label="Blue baseball cap" style="background:radial-gradient(circle at 50% 40%,#3a6bb4,#1f447e)"></div><div class="product-name">Lorem ipsum dolor sit</div><div class="product-price">$25.99</div><div class="btn-cart">ADD TO CART</div></div>
<div class="abs product" style="left:632px;top:2272px"><div class="product-img" role="img" aria-label="Wooden baseball bat with black grip" style="background:linear-gradient(135deg,#f6f3f3 30%,#d9a461 50%,#f6f3f3 70%)"></div><div class="product-name">Lorem ipsum dolor sit</div><div class="product-price">$25.99</div><div class="btn-cart">ADD TO CART</div></div>
<div class="abs product" style="left:879px;top:2272px"><div class="product-img" role="img" aria-label="Natural wood baseball bat" style="background:linear-gradient(135deg,#f6f3f3 30%,#e2b97d 50%,#f6f3f3 70%)"></div><div class="product-name">Lorem ipsum dolor sit</div><div class="product-price">$25.99</div><div class="btn-cart">ADD TO CART</div></div>

<!-- Brands -->
<h2 class="abs section-title" style="top:2678px">OUR BRANDS</h2>
<div class="abs rule" style="left:573px;top:2740px"></div>
<div class="abs partners">
  <span>Ledgerline</span><span>Fitwell</span><span>Kilnworks</span><span>Basicalia</span><span>Market Desk</span><span>Harborstay</span><span>Auralo</span>
</div>

<!-- Footer -->
<footer class="abs footer"></footer>
<div class="abs footer-brand"><div class="brand-mark"></div><div class="brand-name">WREN SPORTING GOODS</div></div>
<nav class="abs footer-nav"><a>HOME</a><a>LOCKER ROOM</a><a>CUSTOM UNIFORMS</a><a>CUSTOM SHIRT CREATOR</a><a>BRANDS</a><a>ABOUT</a></nav>
<div class="abs follow"><b>FOLLOW US</b><span class="social"></span><span class="social"></span><span class="social"></span><span class="social"></span><span class="social"></span></div>
<div class="abs copyright">COPYRIGHT © 2025 ALL RIGHTS RESERVED</div>

</body>
</html>
```